Business Card Design Project

KV Strategy Partners is a management consulting business with C-suite (CEO/CFO etc) target clients. Logo selected is blue with simple/serious typefaces.

Target Market(s)

CEOs and CFOs of large corporates

Industry/Entity Type

Management Consulting

Font styles to use
Serif

Colors
3276b5

Requirements
Must have
• Tag line: Building successful collaborations (use different font)
Address: 457 Cedar Brook Lane #03-22 Singapore 519307
Telephone: +65 8372 6094
Email: kvlorne@mailbox47.com

```html
<!DOCTYPE html>
<html lang="en">
<head>
<meta charset="utf-8">
<title>KV Strategy Partners – Business Cards</title>
<link href="https://fonts.googleapis.com/css2?family=Cormorant+Garamond:wght@500&family=Questrial&display=swap" rel="stylesheet">
<style>
  :root {
    --navy: #0f3762;
    --white: #ffffff;
    --paper: #fbfbfc;
    --stage-light: #f4f4f5;
    --stage-dark: #d9dadc;
  }
  * { margin: 0; padding: 0; box-sizing: border-box; }
  html, body {
    width: 1034px;
    height: 1200px;
    overflow: hidden;
  }
  body {
    background: radial-gradient(ellipse at center, var(--stage-light) 40%, var(--stage-dark) 100%);
    position: relative;
  }
  .card {
    position: absolute;
    left: 160px;
    width: 691px;
    height: 400px;
    overflow: hidden;
  }
  .card--front { top: 135px; background: var(--navy); }
  .card--back  { top: 668px; background: var(--paper); }
  .card__wave {
    position: absolute;
    inset: 0;
    width: 100%;
    height: 100%;
  }
  .brand-name {
    position: absolute;
    font-family: "Cormorant Garamond", Georgia, serif;
    font-weight: 500;
    font-size: 46px;
    letter-spacing: 1px;
    white-space: nowrap;
  }
  .card--front .brand-name {
    color: var(--white);
    top: 100px;
    left: 0;
    right: 0;
    text-align: center;
  }
  .card--back .brand-name {
    color: var(--navy);
    top: 75px;
    left: 58px;
  }
  .tagline {
    position: absolute;
    left: 0;
    right: 0;
    top: 336px;
    text-align: center;
    font-family: "Questrial", Arial, sans-serif;
    font-size: 22px;
    color: var(--navy);
  }
  .contact {
    position: absolute;
    left: 0;
    right: 0;
    top: 268px;
    text-align: center;
    font-family: "Questrial", Arial, sans-serif;
    font-size: 19px;
    line-height: 28px;
    color: var(--white);
    font-style: normal;
  }
</style>
</head>
<body>
  <section class="card card--front">
    <svg class="card__wave" viewBox="0 0 691 400" preserveAspectRatio="none" aria-hidden="true">
      <path d="M0,318 C140,260 290,345 440,300 C560,262 640,236 691,240 L691,400 L0,400 Z" fill="var(--white)"/>
    </svg>
    <div class="brand-name">KV Strategy Partners</div>
    <p class="tagline">Building successful collaborations</p>
  </section>

  <section class="card card--back">
    <svg class="card__wave" viewBox="0 0 691 400" preserveAspectRatio="none" aria-hidden="true">
      <path d="M0,180 C150,205 280,240 420,220 C540,202 620,190 691,200 L691,400 L0,400 Z" fill="var(--navy)"/>
    </svg>
    <div class="brand-name">KV Strategy Partners</div>
    <address class="contact">
      457 Cedar Brook Lane #03-22 Singapore 519307<br>
      Telephone: +65 8372 6094<br>
      kvlorne@mailbox47.com
    </address>
  </section>
</body>
</html>
```